Oral Surgery Office Referral Form and Stationary designs.

Hi, I am a dentist/oral surgeon recently graduated and starting my own practice. Need help in designing an attractive, warm, appealing and Professional referral form (double sided), and stationary design. These will be used for Thank you notes, Professional letters, Front of a presentation folder, Notepads, envelopes, promotional products, Fax, etc... I do have a sample of a typical referral form and also have a logo as well as business card design that I will provide as a base to use. I will attach the files to this posting. Please, do some investigating on the Oral surgery / dental specialist websites as to some of the examples of the referral forms. Thanks and feel free to respond with any questions. Look forward to the designs - having the business card designed here was a great experience.
I will attach more files to clarify / show examples.

HELLO ALL,

I JUST WENT THROUGH THE BRIEF AND REALISED THAT THERE IS A MISTAKE IN MY POSTING. 
THE WEBSITE ADDRESS SHOULD READ:
 WWW.KRELDAX.COM 
IN MY ORIGINAL POSTING IT WAS MISSING THE "M".

TRULY APOLOGIZE FOR ANY INCONVENIENCE.
THANK YOU,
GERALD

Target Market(s)

Dental Professionals and oral surgery patients.

Industry/Entity Type

Dental

Requirements
Must have
• Has to have pictures of the mouth / teeth numbers/ map with directions. Needs to be warm and appealing. If possible to have it in a format that can be easily converted to a clickable one online. Don't know if possible. Thanks.
Should not have
• Typical dental designs .

```html
<!DOCTYPE html>
<html lang="en">
<head>
<meta charset="utf-8">
<title>Brookline Oral Surgery – Stationery</title>
<link href="https://fonts.googleapis.com/css2?family=PT+Sans:wght@400;700&display=swap" rel="stylesheet">
<style>
  :root {
    --ink: #1a1a1a;
    --brand-blue: #1b5fd0;
    --deep-blue: #1a2f9e;
    --bar-blue: #1e88d8;
    --wave: #cfeaf3;
    --paper: #ffffff;
    --edge: #1ba3c6;
    --square: #1d3f8f;
  }
  * { margin: 0; padding: 0; box-sizing: border-box; }
  html, body { width: 916px; height: 1200px; overflow: hidden; background: var(--paper); }
  body { position: relative; font-family: "PT Sans", sans-serif; color: var(--ink); }

  .board-wave { position: absolute; left: 0; top: 0; width: 916px; height: 340px; }

  .brand { position: absolute; display: flex; align-items: center; gap: 8px; }
  .brand-mark { background: var(--square); flex: none; }
  .brand-name { font-weight: 400; color: var(--brand-blue); white-space: nowrap; line-height: 1; }

  .board-brand { right: 32px; top: 60px; }
  .board-brand .brand-mark { width: 44px; height: 44px; }
  .board-brand .brand-name { font-size: 32px; }

  .letterhead {
    position: absolute; left: 160px; top: 240px; width: 597px; height: 840px;
    background: var(--paper); border: 1px solid var(--edge); overflow: hidden;
  }
  .letterhead .side-bar { position: absolute; right: 0; top: 0; width: 15px; height: 100%; background: var(--bar-blue); }
  .letterhead .sheet-wave { position: absolute; left: 0; top: 110px; width: 582px; height: 130px; }
  .letterhead .brand { right: 44px; top: 34px; }
  .letterhead .brand-mark { width: 26px; height: 26px; }
  .letterhead .brand-name { font-size: 18px; }

  .footer { position: absolute; left: 0; right: 15px; text-align: center; }
  .letterhead .footer { bottom: 20px; }
  .signatory { font-size: 12px; font-weight: 700; color: var(--ink); margin-bottom: 14px; }
  .contact { font-size: 10px; font-weight: 700; color: var(--deep-blue); letter-spacing: 0.4px; }
  .contact .dot { display: inline-block; width: 4px; height: 4px; background: var(--bar-blue); margin: 0 14px; vertical-align: middle; }

  .envelope {
    position: absolute; left: 40px; top: 600px; width: 740px; height: 300px;
    background: var(--paper); border: 1px solid var(--edge); overflow: hidden;
  }
  .envelope .side-bar { position: absolute; right: 0; top: 0; width: 16px; height: 100%; background: linear-gradient(180deg, var(--deep-blue), var(--bar-blue)); }
  .envelope .sheet-wave { position: absolute; left: 0; top: 140px; width: 724px; height: 110px; }
  .envelope .brand { left: 30px; bottom: 26px; }
  .envelope .brand-mark { width: 24px; height: 24px; }
  .envelope .brand-name { font-size: 17px; }
  .envelope .footer { left: 250px; right: 16px; bottom: 26px; text-align: left; }
  .envelope .signatory { margin-bottom: 8px; }
  .envelope .contact .dot { margin: 0 10px; }
</style>
</head>
<body>
  <svg class="board-wave" viewBox="0 0 916 340" aria-hidden="true">
    <defs>
      <linearGradient id="boardWaveFill" x1="0" x2="1" y1="0" y2="0">
        <stop offset="0" stop-color="#cfeaf3"/>
        <stop offset="0.6" stop-color="#f2fafc"/>
        <stop offset="1" stop-color="#cfeaf3"/>
      </linearGradient>
    </defs>
    <path d="M0 45 C180 0 360 60 560 140 C720 205 840 240 916 250 L916 320 C820 300 700 250 560 210 C360 150 180 110 0 130 Z" fill="url(#boardWaveFill)"/>
  </svg>

  <div class="brand board-brand">
    <span class="brand-mark"></span>
    <span class="brand-name">Brookline Oral Surgery</span>
  </div>

  <section class="letterhead">
    <svg class="sheet-wave" viewBox="0 0 582 130" preserveAspectRatio="none" aria-hidden="true">
      <path d="M0 110 C140 20 320 10 582 70 L582 110 C380 60 200 55 0 130 Z" fill="var(--wave)"/>
    </svg>
    <div class="brand">
      <span class="brand-mark"></span>
      <span class="brand-name">Brookline Oral Surgery</span>
    </div>
    <div class="side-bar"></div>
    <div class="footer">
      <p class="signatory">Gerald I. Halvorsen DDS, MD</p>
      <p class="contact">2250 Alder Lane, Lincoln, NE 68510<span class="dot"></span>P (402) 555 0148<span class="dot"></span>F (402) 555 0149<span class="dot"></span>WWW.KRELDAX.COM</p>
    </div>
  </section>

  <section class="envelope">
    <svg class="sheet-wave" viewBox="0 0 724 110" preserveAspectRatio="none" aria-hidden="true">
      <path d="M0 90 C160 20 380 0 724 60 L724 95 C460 50 220 50 0 110 Z" fill="var(--wave)"/>
    </svg>
    <div class="brand">
      <span class="brand-mark"></span>
      <span class="brand-name">Brookline Oral Surgery</span>
    </div>
    <div class="side-bar"></div>
    <div class="footer">
      <p class="signatory">Gerald I. Halvorsen DDS, MD</p>
      <p class="contact">2250 Alder Lane, Lincoln, NE 68510<span class="dot"></span>P (402) 555 0148<span class="dot"></span>F (402) 555 0149<span class="dot"></span>WWW.KRELDAX.COM</p>
    </div>
  </section>
</body>
</html>
```